Brightwave MolarNet IT Inc. new website

i need a website for my company which is dedicated to installation and service of computer systems in Dental Offices. I would like for it to encompass a technology feel and professional look. The company deals with all aspects of technology like, Audio Visual, computer systems and networks, Cloud services like data backup, data center. We provide manage services, support and services to Dental Professionals.
Updates

Looking for a Technology font but professional look Added Wednesday, April 20, 2016

Target Market(s)

Dental, Dentist

Industry/Entity Type

Dental

Number of Pages Required

5+ page

Font styles to use
Other font styles liked:
• Futuristic or Techy

Colors
0255a3
ec1f27

Requirements
Must have
• Tabs
Nice to have
• Have no idea maybe some suggestion on your part may help
Should not have
• A professional feel but have a techy look

Files

```html
<!DOCTYPE html>
<html lang="en">
<head>
<meta charset="utf-8">
<title>Brightwave MolarNet IT Inc. – Contact Us</title>
<link rel="stylesheet" href="https://fonts.googleapis.com/css2?family=Exo+2:wght@500;600;700&family=Lato:wght@400;700&family=Roboto:wght@700&family=Crimson+Text&display=swap">
<style>
:root{
  --brand:#0255a3;
  --bar:#0a78bf;
  --accent:#ec1f27;
  --ink:#111;
  --muted:#666;
  --field:#eeeeee;
  --field-line:#d8d8d8;
  --foot:#353535;
  --foot-dark:#222;
  --foot-field:#262626;
  --foot-text:#e6e6e6;
}
*{box-sizing:border-box;margin:0;padding:0}
html,body{width:922px;height:1200px;overflow:hidden}
body{position:relative;background:#fff;font-family:"Lato",sans-serif;color:var(--ink)}
.abs{position:absolute}

.top-bar{left:0;top:0;width:922px;height:30px;background:var(--bar)}
.top-phone{left:606px;top:5px;color:#fff;font:500 15px "Exo 2",sans-serif;display:flex;align-items:center;gap:6px;letter-spacing:.5px}
.social{display:flex;gap:6px}
.top-bar .social{position:absolute;left:742px;top:5px}
.social span{width:20px;height:20px;border-radius:3px;display:block;border:1px solid rgba(255,255,255,.8)}
.s1{background:#3b5998}.s2{background:#2aa3ef}.s3{background:var(--accent)}

.header{left:0;top:30px;width:922px;height:88px;background:#fff}
.logo{left:100px;top:28px;display:flex;align-items:center;gap:8px;font:700 17px "Exo 2",sans-serif;color:var(--brand);line-height:1.05}
.logo i{width:14px;height:14px;background:var(--brand);display:block;border-radius:2px}
.nav{left:356px;top:32px;display:flex;align-items:center;font:700 12px "Exo 2",sans-serif;letter-spacing:.3px}
.nav a{color:var(--ink);text-decoration:none;padding:0 23px;border-left:1px solid #9ac;line-height:14px}
.nav a:first-child{border:none;padding-left:0}
.nav a.active{color:var(--bar)}

.hero{left:0;top:118px;width:922px;height:230px;background:linear-gradient(90deg,#b8bcc2 0%,#5b6a86 20%,#2b3d63 45%,#1f3157 70%,#3a4965 100%)}
.hero-line1{left:238px;top:30px;color:#fff;font:700 29px "Exo 2",sans-serif}
.hero-box{left:369px;top:72px;width:519px;height:88px;border:1px solid rgba(255,255,255,.45);background:rgba(10,50,120,.35)}
.hero-support{left:389px;top:80px;color:#fff;font:700 53px "Roboto",sans-serif;letter-spacing:1px}
.hero-icons{left:670px;top:84px;display:flex;gap:8px}
.hero-icons span{width:63px;height:63px;border-radius:50%;border:4px solid #fff;background:#1d4f9a;display:block}
.hero-line3{left:391px;top:164px;color:#fff;font:700 29px "Exo 2",sans-serif}

.page-title{left:0;top:380px;width:922px;text-align:center;font:700 28px "Exo 2",sans-serif}
.rule{left:288px;top:436px;width:346px;height:1px;background:#ccc}
.rule-mark{left:454px;top:429px;width:15px;height:13px;background:#777;border-radius:2px}

.info-row{left:160px;width:270px;display:flex;gap:10px;font-size:12px;color:var(--muted);line-height:17px}
.info-row svg{flex:none;margin-top:2px}
.info-row b{color:var(--ink);font-weight:400}
.info-row .big{color:var(--ink);font-weight:700}
.info-row .em{color:var(--ink)}
.map{left:444px;top:483px;width:338px;height:143px;background:linear-gradient(135deg,#e8e4d8,#d8e6c8 55%,#a9c8f0 80%,#e9e5da)}

.form-box{left:152px;top:675px;width:618px;height:164px;border:1px solid #ccc;border-radius:6px;background:#fff}
.notch{left:450px;top:662px;width:20px;height:20px;background:#fff;border-left:1px solid #ccc;border-top:1px solid #ccc;transform:rotate(45deg)}
.form-title{left:152px;top:690px;width:618px;text-align:center;font:20px "Crimson Text",serif}
.field{background:var(--field);border:1px solid var(--field-line);font-size:12px;color:#777;padding:6px 7px;border-radius:2px}
.send{left:675px;top:767px;width:71px;height:50px;background:var(--brand);color:#fff;font:700 15px "Lato",sans-serif;display:flex;align-items:center;justify-content:center;border-radius:2px}

.footer{left:0;top:876px;width:922px;height:286px;background:radial-gradient(ellipse at 50% 40%,#444,var(--foot) 60%,#2b2b2b)}
.foot-h{color:#fff;font:600 15px "Exo 2",sans-serif;padding-bottom:8px;border-bottom:1px dotted #777}
.foot-links{left:103px;top:960px;color:var(--foot-text);font-size:12px}
.foot-links li{list-style:none;margin-bottom:17px}
.foot-links li::before{content:"›";margin-right:6px}
.vsep{width:2px;height:160px;background:#2a2a2a;box-shadow:1px 0 0 #4a4a4a}
.foot-contact{left:262px;top:960px;width:190px;color:var(--foot-text);font-size:12px;line-height:15px}
.foot-contact .row{display:flex;gap:14px;margin-bottom:28px}
.foot-contact svg{flex:none;margin-top:1px}
.foot-field{background:var(--foot-field);color:#bbb;font-size:11px;padding:5px 10px;width:187px;height:23px;margin-bottom:4px}
.submit{left:481px;top:1107px;width:73px;height:25px;background:var(--brand);color:#fff;font:700 14px "Lato",sans-serif;display:flex;align-items:center;justify-content:center}
.foot-logo{left:706px;top:960px;width:135px;text-align:center;color:#8a8a8a;font:700 16px "Exo 2",sans-serif;line-height:1.2}
.foot-logo i{display:block;width:46px;height:40px;margin:0 auto 8px;background:#707070;border-radius:5px}
.footer-social{left:733px;top:1075px}
.copyright{left:0;top:1162px;width:922px;height:38px;background:var(--foot-dark);color:#ddd;font-size:11px;display:flex;align-items:center;justify-content:center}
</style>
</head>
<body>

<div class="abs top-bar">
  <div class="abs top-phone">
    <svg width="18" height="18" viewBox="0 0 18 18"><circle cx="9" cy="9" r="8" fill="none" stroke="#fff" stroke-width="1.5"/><path d="M6 5l2 2-1 1.2c.6 1.2 1.6 2.2 2.8 2.8L11 10l2 2-1.3 1.3C8.8 13 5 9.2 4.7 6.3z" fill="#fff"/></svg>
    555-013-2468
  </div>
  <div class="social" aria-label="Social links"><span class="s1"></span><span class="s2"></span><span class="s3"></span></div>
</div>

<header class="abs header">
  <div class="abs logo"><i></i><span>Brightwave<br>MolarNet IT Inc.</span></div>
  <nav class="abs nav">
    <a href="#" aria-label="Home"><svg width="22" height="18" viewBox="0 0 22 18"><path d="M11 1L1 10h3v7h5v-5h4v5h5v-7h3z" fill="#111"/></svg></a>
    <a href="#">ABOUT US</a>
    <a href="#">SERVICES</a>
    <a href="#">SUPPORT</a>
    <a href="#" class="active">CONTACT US</a>
  </nav>
</header>

<section class="abs hero" role="img" aria-label="Dental treatment chair beside a professional in a suit pointing forward">
  <div class="abs hero-line1">We Provide Manage Services,</div>
  <div class="abs hero-box"></div>
  <div class="abs hero-support">SUPPORT</div>
  <div class="abs hero-icons"><span></span><span></span><span></span></div>
  <div class="abs hero-line3">&amp; Service To Dental Professionals.</div>
</section>

<h1 class="abs page-title">Contact Us</h1>
<div class="abs rule"></div>
<div class="abs rule-mark"></div>

<div class="abs info-row" style="top:485px">
  <svg width="12" height="16" viewBox="0 0 12 16"><path d="M6 0a6 6 0 0 0-6 6c0 4.5 6 10 6 10s6-5.5 6-10a6 6 0 0 0-6-6zm0 8.5A2.5 2.5 0 1 1 6 3.5a2.5 2.5 0 0 1 0 5z" fill="#0a78bf"/></svg>
  <div><b>Brightwave MolarNet IT Inc.,</b><br>2150 Harbor Crest Blvd – Ste 210<br>Lakeview, MN 55990</div>
</div>
<div class="abs info-row" style="top:543px">
  <svg width="12" height="14" viewBox="0 0 12 14"><path d="M2 0l3 3-1.5 1.8c.8 2 2.3 3.6 4.3 4.5L9.5 8 12 11l-2 2C5 12.5 .5 8 0 2z" fill="#0a78bf"/></svg>
  <div>Call Us Anytime<br><span class="big">555.013.2468</span></div>
</div>
<div class="abs info-row" style="top:596px">
  <svg width="12" height="10" viewBox="0 0 12 10"><rect width="12" height="10" fill="#0a78bf"/><path d="M0 0l6 5 6-5" fill="none" stroke="#fff"/></svg>
  <div>Write To Us<br><span class="em">hello@brightwavemolarnet.com</span></div>
</div>

<div class="abs map" role="img" aria-label="Road map of the upper Midwest marking the office location"></div>

<div class="abs form-box"></div>
<div class="abs notch"></div>
<div class="abs form-title">Send Us Your Suggestions Or Queries</div>
<div class="abs field" style="left:177px;top:727px;width:181px;height:26px">Name</div>
<div class="abs field" style="left:372px;top:727px;width:181px;height:26px">Email Address</div>
<div class="abs field" style="left:566px;top:727px;width:181px;height:26px">Phone Number</div>
<div class="abs field" style="left:177px;top:767px;width:483px;height:50px">Message</div>
<div class="abs send">SEND</div>

<footer class="abs footer">
  <div class="abs foot-h" style="left:103px;top:32px;width:105px">Quick Links</div>
  <div class="abs foot-h" style="left:261px;top:32px;width:158px">Contact Details</div>
  <div class="abs foot-h" style="left:483px;top:32px;width:185px">Quick Inquiry</div>
  <div class="abs vsep" style="left:234px;top:74px"></div>
  <div class="abs vsep" style="left:456px;top:74px"></div>
  <div class="abs vsep" style="left:696px;top:74px"></div>
</footer>

<ul class="abs foot-links">
  <li style="font-weight:700;color:#fff">Home</li>
  <li>About Us</li>
  <li>Services</li>
  <li>Support</li>
  <li>Contact Us</li>
</ul>

<div class="abs foot-contact">
  <div class="row">
    <svg width="10" height="13" viewBox="0 0 12 16"><path d="M6 0a6 6 0 0 0-6 6c0 4.5 6 10 6 10s6-5.5 6-10a6 6 0 0 0-6-6zm0 8.5A2.5 2.5 0 1 1 6 3.5a2.5 2.5 0 0 1 0 5z" fill="#fff"/></svg>
    <div><b>Brightwave MolarNet IT Inc.</b><br>2150 Harbor Crest Blvd – Ste 210<br>Lakeview, MN 55990</div>
  </div>
  <div class="row">
    <svg width="10" height="12" viewBox="0 0 12 14"><path d="M2 0l3 3-1.5 1.8c.8 2 2.3 3.6 4.3 4.5L9.5 8 12 11l-2 2C5 12.5 .5 8 0 2z" fill="#fff"/></svg>
    <b>555.013.2468</b>
  </div>
  <div class="row">
    <svg width="13" height="10" viewBox="0 0 12 10"><rect x=".5" y=".5" width="11" height="9" fill="none" stroke="#fff"/><path d="M.5 .5l5.5 5 5.5-5" fill="none" stroke="#fff"/></svg>
    <span>hello@brightwavemolarnet.com</span>
  </div>
</div>

<div class="abs" style="left:481px;top:962px">
  <div class="foot-field">Name</div>
  <div class="foot-field">Email</div>
  <div class="foot-field">Phone</div>
  <div class="foot-field" style="height:58px">Message</div>
</div>
<div class="abs submit">SUBMIT</div>

<div class="abs foot-logo"><i></i>Brightwave<br>MolarNet IT Inc.</div>
<div class="abs social footer-social" aria-label="Social links"><span class="s1"></span><span class="s2"></span><span class="s3"></span></div>

<div class="abs copyright">copyright © 2016 Brightwave MolarNet IT Inc. ALL RIGHT RESERVED</div>

</body>
</html>
```